I'm having trouble getting a color gradient for the font on my business card and voucher. I used to have a program that worked, but I can't find it anymore. I hope you can help me. I'm uploading the original, which still has the color gradient, as an example. All of my text should be designed with the color gradient.

```html
<!DOCTYPE html>
<html lang="de">
<head>
<meta charset="utf-8">
<title>Veltra E-Technik – Visitenkarte</title>
<link href="https://fonts.googleapis.com/css2?family=Arimo:wght@700&display=swap" rel="stylesheet">
<style>
  :root {
    --red: #ec1c24;
    --black: #0a0a0a;
    --white: #ffffff;
    --appliance: #d4d5d7;
    --appliance-dark: #a9abae;
    --text-gradient: linear-gradient(180deg, var(--red) 0%, var(--red) 40%, var(--black) 100%);
  }
  html, body {
    margin: 0;
    padding: 0;
    width: 1049px;
    height: 1200px;
    overflow: hidden;
    background: var(--white);
    font-family: "Arimo", Arial, sans-serif;
    font-weight: 700;
  }
  .card {
    position: absolute;
    left: 46px;
    width: 965px;
    box-sizing: border-box;
    border: 4px solid;
    border-image: linear-gradient(180deg, var(--red) 0%, var(--red) 55%, var(--black) 85%, var(--black) 100%) 1;
    background: var(--white);
  }
  .card--front { top: 38px; height: 547px; }
  .card--back { top: 613px; height: 547px; }

  .appliances { position: absolute; left: 0; top: 0; width: 100%; height: 100%; pointer-events: none; }
  .appliance {
    position: absolute;
    box-sizing: border-box;
    border: 2px solid var(--black);
    border-radius: 9px;
    background: linear-gradient(160deg, #eceded 0%, var(--appliance) 55%, var(--appliance-dark) 100%);
  }

  .gradient-text {
    background: var(--text-gradient);
    -webkit-background-clip: text;
    background-clip: text;
    color: transparent;
    -webkit-text-fill-color: transparent;
  }

  .company-name {
    position: absolute;
    left: 156px;
    top: 200px;
    margin: 0;
    font-size: 48px;
    line-height: 56px;
    letter-spacing: 0.5px;
    white-space: nowrap;
  }
  .contact-block {
    position: absolute;
    margin: 0;
    font-size: 16.5px;
    line-height: 21.5px;
    font-style: normal;
    white-space: nowrap;
  }
  .contact-block span { display: block; }
  .address { left: 156px; top: 282px; }
  .office { left: 516px; top: 282px; }
  .manager { left: 157px; top: 436px; }
  .manager-address { left: 309px; top: 431px; }

  .brand {
    position: absolute;
    left: 0;
    width: 100%;
    top: 215px;
    display: flex;
    align-items: center;
    justify-content: center;
    gap: 18px;
  }
  .brand-dot {
    width: 44px;
    height: 44px;
    border-radius: 50%;
    background: var(--red);
  }
  .brand-name {
    font-size: 72px;
    line-height: 80px;
    color: var(--red);
    letter-spacing: 2px;
  }
  .tagline {
    position: absolute;
    left: 0;
    width: 100%;
    top: 480px;
    margin: 0;
    text-align: center;
    font-size: 22px;
    line-height: 28px;
  }
  .tagline span { display: inline-block; }
</style>
</head>
<body>

<section class="card card--front">
  <div class="appliances">
    <div class="appliance" style="left:104px;top:58px;width:68px;height:99px;" role="img" aria-label="Kühlschrank"></div>
    <div class="appliance" style="left:190px;top:86px;width:69px;height:71px;" role="img" aria-label="Einbaubackofen"></div>
    <div class="appliance" style="left:281px;top:83px;width:68px;height:74px;" role="img" aria-label="Geschirrspüler"></div>
    <div class="appliance" style="left:371px;top:83px;width:68px;height:74px;" role="img" aria-label="Herd mit Kochfeld"></div>
    <div class="appliance" style="left:462px;top:82px;width:68px;height:75px;" role="img" aria-label="Waschmaschine"></div>
    <div class="appliance" style="left:552px;top:83px;width:72px;height:74px;" role="img" aria-label="Wäschetrockner"></div>
    <div class="appliance" style="left:645px;top:83px;width:75px;height:74px;" role="img" aria-label="Dunstabzugshaube"></div>
    <div class="appliance" style="left:737px;top:83px;width:76px;height:74px;" role="img" aria-label="Mikrowelle"></div>
  </div>

  <h1 class="company-name gradient-text">VELTRA - E- TECHNIK GmbH</h1>

  <address class="contact-block address">
    <span class="gradient-text">Lindenweg 14</span>
    <span class="gradient-text">41836 Feldhausen</span>
  </address>

  <address class="contact-block office">
    <span class="gradient-text">Telefon Büro:</span>
    <span class="gradient-text">02161 5550142</span>
    <span class="gradient-text">besetzt Mo-Fr von 18-20 Uhr</span>
    <span class="gradient-text">info@veltra-technik.de</span>
  </address>

  <address class="contact-block manager">
    <span class="gradient-text">Geschäftsführer :</span>
    <span class="gradient-text">Jonas Martin Keller</span>
    <span class="gradient-text">01515 5527384</span>
  </address>

  <address class="contact-block manager-address">
    <span class="gradient-text">Lindenweg 14</span>
  </address>
</section>

<section class="card card--back">
  <div class="appliances">
    <div class="appliance" style="left:94px;top:34px;width:69px;height:101px;" role="img" aria-label="Kühlschrank"></div>
    <div class="appliance" style="left:181px;top:68px;width:70px;height:67px;" role="img" aria-label="Einbaubackofen"></div>
    <div class="appliance" style="left:273px;top:62px;width:70px;height:73px;" role="img" aria-label="Geschirrspüler"></div>
    <div class="appliance" style="left:365px;top:62px;width:70px;height:73px;" role="img" aria-label="Herd mit Kochfeld"></div>
    <div class="appliance" style="left:456px;top:61px;width:70px;height:74px;" role="img" aria-label="Waschmaschine"></div>
    <div class="appliance" style="left:548px;top:62px;width:74px;height:73px;" role="img" aria-label="Wäschetrockner"></div>
    <div class="appliance" style="left:642px;top:62px;width:77px;height:73px;" role="img" aria-label="Dunstabzugshaube"></div>
    <div class="appliance" style="left:735px;top:62px;width:77px;height:73px;" role="img" aria-label="Mikrowelle"></div>
  </div>

  <div class="brand">
    <span class="brand-dot"></span>
    <span class="brand-name">VELTRA</span>
  </div>

  <p class="tagline"><span class="gradient-text">Haushaltsgeräte reparieren statt wegwerfen!</span></p>
</section>

</body>
</html>
```